Classy, Elegant, Simple Business Card Design

Looking to have a classy, simple, and elegant design. Want a top notch designed business card. I really like the look of the new brivo credit card. I also like the design I attached. I am trying to reach 21-29 year old females for booking us for there wedding or event. We offer Disc Jockey Service, Photo Booth Rentals, and Uplighting .

Target Market(s)

21-28 year old females

Contact Information for Business Card

Has to have logo, website, email, and phone number

Font styles to use
Other font styles liked:
• open to font choice, modern, clean
Designer to choose
33a6d7
0791cd
0555a3
ffffff

Requirements
Must have
• Has to have logo, website, email, and phone number
Nice to have
• I really like the design of the new brivo credit card. I also included my logo and some designs I like
Should not have
• clutter or too much info

```html
<!DOCTYPE html>
<html lang="en">
<head>
<meta charset="UTF-8">
<title>Tidebeat Event Group – Business Card</title>
<link href="https://fonts.googleapis.com/css2?family=Jost:wght@400;500;700&display=swap" rel="stylesheet">
<style>
  :root {
    --backdrop: #1b1d22;
    --card-navy: #123c73;
    --card-navy-deep: #0d2f5e;
    --pattern-blue: #1d4f8f;
    --accent-sky: #33a6d7;
    --accent-blue: #0791cd;
    --accent-deep: #0555a3;
    --ink-white: #ffffff;
    --ink-muted: #8fa6c4;
  }
  * { margin: 0; padding: 0; box-sizing: border-box; }
  html, body {
    width: 1200px;
    height: 900px;
    overflow: hidden;
    background: var(--backdrop);
    font-family: "Jost", "Futura", sans-serif;
  }
  .sheet {
    width: 1200px;
    height: 900px;
    display: flex;
    flex-direction: column;
    align-items: center;
    justify-content: center;
    gap: 56px;
  }
  .card {
    position: relative;
    width: 620px;
    height: 354px;
    background: radial-gradient(circle at 50% 45%, var(--card-navy) 0%, var(--card-navy-deep) 100%);
    border-radius: 4px;
    overflow: hidden;
    box-shadow: 0 18px 40px rgba(0,0,0,0.45);
    color: var(--ink-white);
  }
  .pattern {
    position: absolute;
    width: 300px;
    height: 300px;
    border-radius: 50%;
    background: radial-gradient(circle, var(--pattern-blue) 0%, rgba(29,79,143,0.35) 55%, rgba(29,79,143,0) 72%);
  }
  .pattern--front-right { right: -110px; top: 90px; }
  .pattern--front-bottom { left: 200px; bottom: -190px; }
  .pattern--back-top { left: -120px; top: -130px; }
  .pattern--back-bottom { right: -110px; bottom: -140px; }

  /* Front face */
  .brand-front {
    position: absolute;
    inset: 0;
    display: flex;
    flex-direction: column;
    align-items: center;
    justify-content: center;
  }
  .brand-lockup {
    display: flex;
    align-items: center;
    gap: 14px;
  }
  .brand-dot {
    width: 14px;
    height: 14px;
    border-radius: 50%;
    background: var(--accent-sky);
  }
  .brand-name {
    font-size: 48px;
    font-weight: 500;
    letter-spacing: 3px;
    color: var(--accent-sky);
    line-height: 1;
  }
  .brand-tagline {
    margin-top: 8px;
    font-size: 14px;
    letter-spacing: 9px;
    color: var(--ink-muted);
  }
  .brand-url {
    margin-top: 30px;
    font-size: 18px;
    letter-spacing: 1px;
    color: var(--ink-white);
  }
  .brand-url span { color: var(--accent-blue); font-weight: 500; }

  /* Back face */
  .back-layout {
    position: absolute;
    inset: 0;
    display: flex;
    align-items: center;
    padding: 0 48px;
  }
  .brand-back {
    width: 230px;
    display: flex;
    flex-direction: column;
    align-items: flex-end;
    padding-right: 26px;
  }
  .brand-back .brand-name { font-size: 32px; letter-spacing: 2px; }
  .brand-back .brand-dot { width: 10px; height: 10px; }
  .brand-back .brand-lockup { gap: 10px; }
  .brand-back .brand-tagline { font-size: 10px; letter-spacing: 6px; margin-top: 6px; }
  .divider {
    width: 1px;
    height: 120px;
    background: var(--accent-deep);
  }
  .contact {
    padding-left: 26px;
    display: flex;
    flex-direction: column;
    gap: 8px;
  }
  .contact-name {
    font-size: 28px;
    font-weight: 700;
    letter-spacing: 1px;
    text-transform: uppercase;
    margin-bottom: 6px;
  }
  .contact-line {
    display: flex;
    align-items: center;
    gap: 10px;
    font-size: 17px;
    letter-spacing: 0.5px;
  }
  .contact-line svg { width: 14px; height: 14px; flex: none; }
</style>
</head>
<body>
<main class="sheet">

  <section class="card card--front">
    <div class="pattern pattern--front-right" role="img" aria-label="Decorative fan of soft blue squares"></div>
    <div class="pattern pattern--front-bottom" role="img" aria-label="Decorative fan of soft blue squares"></div>
    <div class="brand-front">
      <div class="brand-lockup">
        <span class="brand-dot"></span>
        <span class="brand-name">TIDEBEAT</span>
      </div>
      <div class="brand-tagline">EVENT GROUP</div>
      <div class="brand-url">www.<span>tidebeat</span>.com</div>
    </div>
  </section>

  <section class="card card--back">
    <div class="pattern pattern--back-top" role="img" aria-label="Decorative fan of soft blue squares"></div>
    <div class="pattern pattern--back-bottom" role="img" aria-label="Decorative fan of soft blue squares"></div>
    <div class="back-layout">
      <div class="brand-back">
        <div class="brand-lockup">
          <span class="brand-dot"></span>
          <span class="brand-name">TIDEBEAT</span>
        </div>
        <div class="brand-tagline">EVENT GROUP</div>
      </div>
      <div class="divider"></div>
      <div class="contact">
        <div class="contact-name">Marlo Vance</div>
        <div class="contact-line">
          <svg viewBox="0 0 24 24" aria-hidden="true"><path fill="#33a6d7" d="M6.6 10.8a15 15 0 0 0 6.6 6.6l2.2-2.2a1 1 0 0 1 1-.25 11.4 11.4 0 0 0 3.6.57 1 1 0 0 1 1 1V20a1 1 0 0 1-1 1A17 17 0 0 1 3 4a1 1 0 0 1 1-1h3.5a1 1 0 0 1 1 1c0 1.25.2 2.45.57 3.57a1 1 0 0 1-.25 1z"/></svg>
          <span>0000 412 587</span>
        </div>
        <div class="contact-line">
          <svg viewBox="0 0 24 24" aria-hidden="true"><rect x="2" y="5" width="20" height="14" rx="1.5" fill="#33a6d7"/><path d="M3 6l9 7 9-7" stroke="#0d2f5e" stroke-width="1.8" fill="none"/></svg>
          <span>hello@tidebeat.com</span>
        </div>
        <div class="contact-line">
          <svg viewBox="0 0 24 24" aria-hidden="true"><circle cx="12" cy="12" r="9.5" fill="none" stroke="#33a6d7" stroke-width="2"/><path d="M2.5 12h19M12 2.5c3 3 3 16 0 19M12 2.5c-3 3-3 16 0 19" stroke="#33a6d7" stroke-width="1.6" fill="none"/></svg>
          <span>www.tidebeat.com</span>
        </div>
      </div>
    </div>
  </section>

</main>
</body>
</html>
```